I need the following
2 versions (CMYK and RGB)
Full Page ad design 7.5" wide x 10" tall
No less than 300 dpi for print and 72dpi for web:
Full Color CMYK for print and RGB for web
Provide a high quality JPEG of the ad as well.

You can use the attached post card as a guide and use the info within it. You can get more information from our website at HaulingCrewFolks.net.
Also add a block with the following ... We work with real estate agents to make moving stress - free for their clients:
*Old Fashioned Customer Service
*Discounted rates
*Always Free Estimates
*Fully Licensed and Insured
*Communication From Start To Finish
*Full Service Moving

```html
<!DOCTYPE html>
<html lang="en">
<head>
<meta charset="utf-8">
<title>Hauling Crew Folks – Full Page Ad</title>
<link rel="stylesheet" href="https://fonts.googleapis.com/css2?family=Montserrat:wght@500;600;800;900&family=Kaushan+Script&display=swap">
<style>
  :root {
    --orange: #f59c4c;
    --charcoal: #333333;
    --white: #ffffff;
    --stage: #d6d6d6;
    --photo-warm: #8a6a55;
    --photo-cool: #7d7a78;
  }
  html, body {
    margin: 0;
    width: 1200px;
    height: 632px;
    overflow: hidden;
    background: var(--stage);
  }
  .ad {
    position: absolute;
    left: 375px;
    top: 16px;
    width: 450px;
    height: 600px;
    box-shadow: 0 4px 14px rgba(0,0,0,.25);
  }
  .headline { font-family: "Montserrat", sans-serif; font-weight: 900; fill: var(--charcoal); }
  .headline--light { fill: var(--white); }
  .perk { font-family: "Montserrat", sans-serif; font-weight: 500; font-size: 10.5px; fill: var(--charcoal); }
  .tagline { font-family: "Kaushan Script", cursive; font-size: 21px; fill: var(--white); stroke: var(--orange); stroke-width: 3px; paint-order: stroke; }
  .brand-name { font-family: "Montserrat", sans-serif; font-weight: 600; font-size: 11px; fill: var(--white); }
  .contact { font-family: "Montserrat", sans-serif; font-weight: 500; font-size: 8.6px; fill: var(--white); }
  .contact--accent { fill: var(--orange); }
</style>
</head>
<body>
<svg class="ad" viewBox="0 0 450 600" xmlns="http://www.w3.org/2000/svg">
  <defs>
    <linearGradient id="crew-photo" x1="0" y1="0" x2="1" y2="1">
      <stop offset="0" stop-color="#c9c2b6"/>
      <stop offset="1" stop-color="var(--photo-warm)"/>
    </linearGradient>
    <linearGradient id="room-photo" x1="0" y1="0" x2="1" y2="1">
      <stop offset="0" stop-color="#d8d0c2"/>
      <stop offset="1" stop-color="#6e4a35"/>
    </linearGradient>
    <linearGradient id="truck-photo" x1="0" y1="0" x2="0" y2="1">
      <stop offset="0" stop-color="#6f6a66"/>
      <stop offset="0.55" stop-color="#9a9591"/>
      <stop offset="1" stop-color="#8a5244"/>
    </linearGradient>
  </defs>

  <!-- base -->
  <rect class="sheet" width="450" height="600" fill="var(--white)"/>

  <!-- headline bands -->
  <polygon class="band band--orange" points="24,0 450,0 450,40 14,40" fill="var(--orange)"/>
  <text class="headline" x="28" y="35" font-size="33" textLength="286" lengthAdjust="spacingAndGlyphs">WE WORK WITH</text>
  <text class="headline" x="28" y="72" font-size="32" textLength="394" lengthAdjust="spacingAndGlyphs">REAL ESTATE AGENTS</text>
  <polygon class="band band--orange" points="6,79 450,79 450,108 0,108" fill="var(--orange)"/>
  <text class="headline" x="29" y="104" font-size="26" textLength="240" lengthAdjust="spacingAndGlyphs">TO MAKE MOVING</text>
  <rect class="band band--dark" y="108" width="450" height="492" fill="var(--charcoal)"/>
  <text class="headline headline--light" x="26" y="159" font-size="52" textLength="396" lengthAdjust="spacingAndGlyphs">STRESS-FREE</text>
  <polygon class="band band--orange" points="0,167 437,167 424,200 0,200" fill="var(--orange)"/>
  <text class="headline" x="28" y="194" font-size="26" textLength="267" lengthAdjust="spacingAndGlyphs">FOR THEIR CLIENTS:</text>

  <!-- service photos -->
  <polygon points="8,215 30,215 10,333 0,333 0,240" fill="var(--orange)"/>
  <polygon points="35,215 42,215 22,333 15,333" fill="var(--white)"/>
  <g role="img" aria-label="Mover in a work jacket wheeling a dolly of boxes through a hallway">
    <polygon points="46,215 120,215 104,333 27,333" fill="url(#crew-photo)"/>
  </g>
  <g role="img" aria-label="Room with packed moving boxes and a potted plant">
    <polygon points="123,215 216,215 200,333 107,333" fill="url(#room-photo)"/>
  </g>

  <!-- perks list -->
  <polygon points="437,210 450,210 450,333 418,333" fill="var(--orange)"/>
  <g class="perks">
    <polygon points="223,215 445,215 440,232 218,232" fill="var(--white)"/>
    <text class="perk" x="240" y="227.5">Old Fashioned Customer Service</text>
    <polygon points="216,235 440,235 435,252 211,252" fill="var(--white)"/>
    <text class="perk" x="234" y="247.5">Discounted rates</text>
    <polygon points="209,255 434,255 429,272 204,272" fill="var(--white)"/>
    <text class="perk" x="227" y="267.5">Always Free Estimates</text>
    <polygon points="203,275 428,275 423,292 198,292" fill="var(--white)"/>
    <text class="perk" x="221" y="287.5">Fully Licensed and Insured</text>
    <polygon points="197,295 423,295 418,312 192,312" fill="var(--white)"/>
    <text class="perk" x="213" y="307.5">Communication From Start To Finish</text>
    <polygon points="191,315 418,315 413,333 186,333" fill="var(--white)"/>
    <text class="perk" x="199" y="328">Full Service Moving</text>
  </g>

  <!-- truck photo -->
  <g role="img" aria-label="White pickup truck parked on a brick driveway with a moving trailer">
    <polygon points="0,336 450,336 450,526 0,526" fill="url(#truck-photo)"/>
  </g>
  <polygon points="0,346 30,346 14,440 0,440" fill="var(--orange)"/>
  <polygon points="450,432 450,506 412,506" fill="var(--white)"/>

  <g transform="rotate(-3 115 450)">
    <text class="tagline" x="20" y="440">Our Backs Are Strong...</text>
    <text class="tagline" x="20" y="467">our Reputation Stronger!</text>
  </g>

  <!-- brand block -->
  <polygon points="28,486 184,486 176,520 20,520" fill="var(--charcoal)"/>
  <polygon points="28,486 34,486 26,520 20,520" fill="var(--white)"/>
  <polygon points="184,486 189,486 181,520 176,520" fill="var(--orange)"/>
  <rect x="48" y="498" width="9" height="9" fill="var(--white)"/>
  <text class="brand-name" x="62" y="507">Hauling Crew Folks</text>

  <!-- contact panel -->
  <polygon points="70,521 210,521 204,527 64,527" fill="var(--white)"/>
  <polygon points="245,521 392,521 390,527 243,527" fill="var(--white)"/>
  <polygon points="390,521 400,521 378,600 362,600" fill="var(--orange)"/>
  <polygon points="372,527 380,527 360,600 352,600" fill="var(--white)"/>
  <polygon points="64,527 72,527 52,600 44,600" fill="var(--white)"/>
  <polygon points="52,540 60,540 44,600 28,600" fill="var(--orange)"/>

  <g class="contacts">
    <circle cx="82" cy="538" r="2" fill="var(--white)"/>
    <text class="contact" x="86" y="541">Address: 4150 Cedar Hollow Ln, Mesquite, TX 75150, United States</text>
    <circle cx="78" cy="553" r="2" fill="var(--white)"/>
    <text class="contact" x="82" y="556">Email: haulingcrewfolks1@mailbox.net</text>
    <circle cx="74" cy="567" r="2" fill="var(--orange)"/>
    <text class="contact contact--accent" x="78" y="570">Call Us: (555) 214-0738</text>
    <circle cx="70" cy="582" r="2" fill="var(--orange)"/>
    <text class="contact contact--accent" x="74" y="585">TxDMV No. 000123456X</text>
    <circle cx="204" cy="567" r="2" fill="var(--orange)"/>
    <text class="contact contact--accent" x="208" y="570">TxDMV Toll-Free 1-800-555-0142</text>
    <circle cx="196" cy="582" r="2" fill="var(--orange)"/>
    <text class="contact contact--accent" x="200" y="585">USDOT: 0000000</text>
  </g>
</svg>
</body>
</html>
```